Design for a Service-Based Estimate

We want a design for an Estimate that will always be sent in PDF format. The estimate or proposal is a critical document that needs to plainly show the service items, item description but also needs to be attractive and professional looking. Our current estimate deliverable is attached but it looks really basic like a Word document

```html
<!DOCTYPE html>
<html lang="en">
<head>
<meta charset="utf-8">
<title>Firm Grade Estimate</title>
<link href="https://fonts.googleapis.com/css2?family=Open+Sans:ital,wght@0,400;0,600;0,700;1,400;1,600;1,700&display=swap" rel="stylesheet">
<style>
  :root {
    --backdrop: #bcc5d4;
    --paper: #ffffff;
    --navy: #2f2b4b;
    --taupe: #978c80;
    --accent: #d9472b;
    --ink: #222034;
    --rule: #9a9a9a;
  }
  * { box-sizing: border-box; margin: 0; padding: 0; }
  html, body { width: 1200px; height: 900px; overflow: hidden; }
  body {
    background: var(--backdrop);
    font-family: "Open Sans", sans-serif;
    color: var(--ink);
    position: relative;
  }
  .estimate-sheet {
    position: absolute;
    left: 300px; top: 22px;
    width: 600px; height: 856px;
    background: var(--paper);
    box-shadow: 0 10px 30px rgba(40, 45, 70, 0.25);
    overflow: hidden;
  }
  .brand-name {
    position: absolute; left: 40px; top: 46px;
    font-weight: 700; font-size: 30px; letter-spacing: 1px;
    color: var(--navy);
  }
  .recipient {
    position: absolute; right: 40px; top: 46px;
    text-align: right; font-style: italic; font-size: 11.5px; line-height: 1.6;
  }
  .recipient .label { margin-right: 4px; }
  .project-heading {
    position: absolute; left: 0; right: 0; top: 150px;
    text-align: center; font-style: italic; font-size: 11.5px; line-height: 1.75;
  }
  .project-heading .project-title { font-weight: 700; }
  .project-heading .bid-number { margin-top: 8px; }
  .line-items {
    position: absolute; left: 36px; right: 36px; top: 232px;
    border-collapse: collapse; font-style: italic; font-size: 11px;
  }
  .line-items th {
    font-weight: 700; text-align: left; padding: 6px 6px;
    border-top: 1px solid var(--rule); border-bottom: 1px solid var(--rule);
    vertical-align: bottom;
  }
  .line-items .head-item { padding-bottom: 26px; }
  .line-items td {
    padding: 8px 6px; border-bottom: 1px solid var(--rule);
    vertical-align: middle; line-height: 1.45;
  }
  .line-items .num { text-align: center; white-space: nowrap; }
  .line-items .amount { text-align: right; font-weight: 700; white-space: nowrap; }
  .line-items .description { width: 370px; }
  .line-items .total-row td { border-bottom: none; font-weight: 700; }
  .line-items .total-label { text-align: right; }
  .sheet-footer { position: absolute; left: 0; bottom: 0; width: 600px; height: 150px; }
  .contact {
    position: absolute; display: flex; align-items: center; gap: 8px;
    font-size: 12px; color: var(--ink);
  }
  .contact-phone { left: 62px; bottom: 76px; }
  .contact-email { left: 232px; bottom: 76px; }
  .web-address {
    position: absolute; right: 30px; bottom: 12px;
    color: #fff; font-size: 12.5px; letter-spacing: 1.5px;
  }
</style>
</head>
<body>
  <main class="estimate-sheet">
    <div class="brand-name">FIRM GRADE</div>

    <address class="recipient">
      <div><span class="label">To:</span> Dale Whitmore</div>
      <div>742 Birch Lane NE Fairview 30418</div>
      <div>dwhitmore@mailbox.net</div>
    </address>

    <header class="project-heading">
      <div class="project-title">Dale Whitmore New Concrete Pad</div>
      <div>742 Birch Lane NE Fairview 30418</div>
      <div class="bid-number">Bid#: 20-0182</div>
    </header>

    <table class="line-items">
      <thead>
        <tr>
          <th class="head-item">Item</th>
          <th class="num">Quantity</th>
          <th class="num">U/M</th>
          <th class="num">Unit $</th>
          <th class="amount">Total $</th>
        </tr>
      </thead>
      <tbody>
        <tr>
          <td class="description">Form, Pour &amp; Finish New Concrete Slab (24' x 24' x 4"). Includes: 3000psi Concrete Mix, Footer (12" x 8") with One (#5) Continuous Rebar, Wire Mesh Reinforcement and Saw-Cut Expansion Joints</td>
          <td class="num">576</td>
          <td class="num">SF</td>
          <td class="num">$8.65</td>
          <td class="amount">$4,982.40</td>
        </tr>
        <tr>
          <td class="description">OPTIONAL: Add (2' x 24' x 4") Small Ramp Area</td>
          <td class="num">48</td>
          <td class="num">SF</td>
          <td class="num">$8.65</td>
          <td class="amount">$415.20</td>
        </tr>
        <tr class="total-row">
          <td></td><td></td>
          <td class="total-label" colspan="2">Total Price</td>
          <td class="amount">$5,397.60</td>
        </tr>
      </tbody>
    </table>

    <footer class="sheet-footer">
      <svg width="600" height="150" viewBox="0 0 600 150" aria-hidden="true">
        <line x1="36" y1="62" x2="34" y2="84" stroke="#d9472b" stroke-width="1.2"/>
        <line x1="202" y1="62" x2="200" y2="84" stroke="#d9472b" stroke-width="1.2"/>
        <polygon points="0,98 340,98 362,124 362,150 0,150" fill="#978c80"/>
        <polygon points="340,98 352,98 376,122 600,122 600,150 362,150 362,124" fill="#fff"/>
        <polygon points="345,110 600,110 600,150 375,150" fill="#2f2b4b"/>
        <polygon points="345,110 375,150 362,150 362,124" fill="#fff"/>
      </svg>
      <div class="contact contact-phone">
        <svg width="11" height="11" viewBox="0 0 24 24" aria-hidden="true"><path fill="#d9472b" d="M6.6 10.8a15.1 15.1 0 0 0 6.6 6.6l2.2-2.2c.3-.3.7-.4 1-.2 1.1.4 2.3.6 3.6.6.6 0 1 .4 1 1V20c0 .6-.4 1-1 1C10.6 21 3 13.4 3 4c0-.6.4-1 1-1h3.5c.6 0 1 .4 1 1 0 1.3.2 2.5.6 3.6.1.3 0 .7-.2 1z"/></svg>
        <span>+1 555-014-2273</span>
      </div>
      <div class="contact contact-email">
        <svg width="13" height="10" viewBox="0 0 26 20" aria-hidden="true"><rect x="1" y="1" width="24" height="18" fill="none" stroke="#d9472b" stroke-width="2"/><path d="M1 1l12 10L25 1" fill="none" stroke="#d9472b" stroke-width="2"/></svg>
        <span>info@firmgrade.com</span>
      </div>
      <div class="web-address">www.firmgrade.com</div>
    </footer>
  </main>
</body>
</html>
```